Ruby Deck Fun Casino Entertainment

Looking to update my business card and make it look more modern, stand out and eye catching.
We are are fun casino business in Australia (primarily Sydney). Blackjack and Roulette are our most popular games although we have pretty much every game available for hire that you would find in a real casino. The final design would need to be sleek and appeal to the more upmarket corporate sector.
We mainly cater for Corporate Events, Private Parties, Fundraising Events, Team Building, Poker Tournaments
I think I'd prefer the colour Black.

Target Market(s)

High-end Corporate

Industry/Entity Type

Events

Contact Information for Business Card

Ned Paxley
Director
1300 472 861
0438 705 705
info@rubydeckfun.com.au
www.rubydeckfun.com.au
Facebook & Instagram @rubydeckshowhire (proper social icons preferred)

Colors
000000
0255a3

Requirements
Must have
• Front side:
• Logo
• Contact details
• 'Australia's #1 Fun Casino Specialists'
• Back:
• Logo
Nice to have
• Back:
• Corporate Events
• Private Parties
• Poker Tournaments
• Fundraising
• Props & Theming
• Photo Booth
• Horse Racing Events
• The Vegas Sign attached, maybe on the back of the card in the background...?

```html
<!DOCTYPE html>
<html lang="en">
<head>
<meta charset="utf-8">
<title>Ruby Deck Fun Casino Entertainment – Business Card</title>
<link rel="stylesheet" href="https://fonts.googleapis.com/css2?family=Open+Sans:wght@400;600;700&display=swap">
<style>
  :root {
    --backdrop: #e4e4e4;
    --card: #2b2b2d;
    --divider: #454547;
    --accent: #f5a71f;
    --text-muted: #c9c9c9;
    --social: #4a63a8;
  }
  * { margin: 0; padding: 0; box-sizing: border-box; }
  html, body { width: 1200px; height: 900px; overflow: hidden; }
  body {
    background: var(--backdrop);
    font-family: "Open Sans", Arial, sans-serif;
    display: flex;
    flex-direction: column;
    align-items: center;
    justify-content: center;
    gap: 40px;
  }
  .card {
    width: 700px;
    height: 390px;
    background: var(--card);
    border-radius: 34px;
    position: relative;
    display: flex;
    box-shadow: 0 10px 24px rgba(0,0,0,0.18);
  }
  .card__logo-area {
    width: 340px;
    display: flex;
    align-items: center;
    justify-content: center;
  }
  .brand-mark {
    display: flex;
    align-items: center;
    gap: 14px;
  }
  .brand-mark__dot {
    width: 44px; height: 44px;
    border-radius: 50%;
    background: var(--accent);
    flex-shrink: 0;
  }
  .brand-mark__name {
    color: var(--accent);
    font-weight: 700;
    font-size: 30px;
    line-height: 1.05;
    text-transform: uppercase;
    letter-spacing: 0.5px;
  }
  .card__divider {
    position: absolute;
    left: 340px;
    top: 70px;
    bottom: 70px;
    width: 1px;
    background: var(--divider);
  }
  .card__content {
    padding-left: 36px;
    display: flex;
    flex-direction: column;
    justify-content: center;
  }
  .services { list-style: none; }
  .services li {
    color: var(--accent);
    font-size: 17px;
    line-height: 1.3;
    text-transform: uppercase;
    display: flex;
    align-items: center;
    gap: 10px;
  }
  .services li::before {
    content: "";
    width: 7px; height: 7px;
    border-radius: 50%;
    background: var(--accent);
  }
  .contact__name {
    color: var(--accent);
    font-weight: 700;
    font-size: 24px;
    text-transform: uppercase;
    line-height: 1.1;
  }
  .contact__role {
    color: var(--text-muted);
    font-size: 16px;
    margin-bottom: 10px;
  }
  .contact__list { list-style: none; }
  .contact__list li {
    color: var(--text-muted);
    font-size: 16px;
    line-height: 1.45;
    display: flex;
    align-items: center;
    gap: 8px;
  }
  .contact__list svg { width: 13px; height: 13px; fill: var(--accent); flex-shrink: 0; }
  .contact__social { margin-top: 10px; }
  .social-dot {
    width: 18px; height: 18px;
    border-radius: 50%;
    background: var(--social);
    flex-shrink: 0;
  }
  .card__tagline {
    position: absolute;
    right: 48px;
    bottom: 34px;
    color: var(--accent);
    font-size: 17px;
    font-weight: 600;
    text-transform: uppercase;
  }
  .card--front .card__content { padding-bottom: 40px; }
</style>
</head>
<body>

  <section class="card card--back" aria-label="Card back">
    <div class="card__logo-area">
      <div class="brand-mark">
        <span class="brand-mark__dot"></span>
        <span class="brand-mark__name">Ruby Deck<br>Productions</span>
      </div>
    </div>
    <div class="card__divider"></div>
    <div class="card__content">
      <ul class="services">
        <li>Corporate Events</li>
        <li>Private Parties</li>
        <li>Poker Tournaments</li>
        <li>Fundraising</li>
        <li>Props &amp; Theming</li>
        <li>Photo Booth</li>
        <li>Horse Racing Events</li>
      </ul>
    </div>
  </section>

  <section class="card card--front" aria-label="Card front">
    <div class="card__logo-area">
      <div class="brand-mark">
        <span class="brand-mark__dot"></span>
        <span class="brand-mark__name">Ruby Deck<br>Productions</span>
      </div>
    </div>
    <div class="card__divider"></div>
    <div class="card__content contact">
      <p class="contact__name">Ned Paxley</p>
      <p class="contact__role">Director</p>
      <ul class="contact__list">
        <li><svg viewBox="0 0 16 16" aria-hidden="true"><path d="M3 1l3 3-2 2c1 2 3 4 6 6l2-2 3 3-2 2C7 15 1 9 1 3z"/></svg>1300 472 861</li>
        <li><svg viewBox="0 0 16 16" aria-hidden="true"><path d="M4 0h8a1 1 0 011 1v14a1 1 0 01-1 1H4a1 1 0 01-1-1V1a1 1 0 011-1zm1 2v10h6V2zm3 11a1 1 0 100 2 1 1 0 000-2z"/></svg>0438 705 705</li>
        <li><svg viewBox="0 0 16 16" aria-hidden="true"><path d="M0 3h16v10H0zm1 1l7 5 7-5z"/></svg>info@rubydeckfun.com.au</li>
        <li><svg viewBox="0 0 16 16" aria-hidden="true"><circle cx="8" cy="8" r="7"/></svg>www.rubydeckfun.com.au</li>
      </ul>
      <ul class="contact__list contact__social">
        <li><span class="social-dot"></span>@rubydeckshowhire</li>
        <li><span class="social-dot"></span>@rubydeckshowhire</li>
      </ul>
    </div>
    <p class="card__tagline">Australia's #1 Fun Casino Specialists</p>
  </section>

</body>
</html>
```